TBNW site redesign

Please redesign a home page with content provided. PSD only - no coding
Can use any images from Vexelmarq.com

Please create a site design that more clearly illustrates the client's services and expertise. We are looking for a high-end design.

Any images used must be generic or of Dallas TX.

Fonts: Any
Colors: Match to logo
Look: Modern - Professional

Target Market(s)

medium-large business owners

Number of Pages Required

1 page

Font styles to use
Serif
Sans Serif

Requirements
Must have
• cohesive professional design
• high end look
• Match to logo

```html
<!DOCTYPE html>
<html lang="en">
<head>
<meta charset="utf-8">
<title>TBNW – Professional Office and Warehouse Leasing</title>
<link href="https://fonts.googleapis.com/css2?family=Montserrat:wght@300;400;500;600;700;800&family=Playfair+Display:wght@400&display=swap" rel="stylesheet">
<style>
:root{
  --red:#f3323d;
  --red-dark:#d72a33;
  --ink:#222222;
  --text:#6f6f6f;
  --white:#ffffff;
  --panel:#e6e6e6;
  --faint:#f2f2f2;
  --sky-a:#1d6fa0;
  --sky-b:#8eaabb;
  --glass:#2f7c9b;
}
*{margin:0;padding:0;box-sizing:border-box}
html,body{width:1200px;height:1200px;overflow:hidden;background:var(--white);font-family:"Montserrat",sans-serif}
.page{position:relative;width:1200px;height:1200px}

.site-header{position:absolute;top:0;left:0;width:1200px;height:64px;background:var(--white)}
.brand{position:absolute;left:158px;top:14px;display:flex;align-items:center;gap:8px}
.brand-mark{width:14px;height:14px;background:var(--red)}
.brand-name{font-family:"Montserrat",sans-serif;font-weight:700;font-size:18px;color:var(--red);letter-spacing:1px}
.main-nav{position:absolute;top:0;left:433px;height:64px;display:flex}
.main-nav a{display:block;height:64px;line-height:64px;padding:0 7px;margin-right:20px;font-size:13.5px;font-weight:500;color:var(--ink);text-decoration:none;position:relative}
.main-nav a.is-active::after{content:"";position:absolute;left:0;right:0;bottom:0;height:3px;background:var(--red)}

.hero{position:absolute;top:64px;left:0;width:1200px;height:520px}
.hero-photo{position:absolute;inset:0;background:linear-gradient(100deg,var(--sky-a) 0%,var(--sky-b) 42%,#7fa3b6 55%,var(--glass) 75%,#1f6c8b 100%)}
.hero-copy{position:absolute;left:156px;top:150px;color:var(--white)}
.hero-title{font-size:40px;line-height:48px;font-weight:300;letter-spacing:.5px}
.hero-title strong{display:block;font-weight:800;letter-spacing:-.5px}
.hero-lead{margin-top:20px;width:570px;font-size:15px;line-height:23px;font-weight:500}
.btn{display:inline-block;background:var(--red);color:var(--white);font-weight:600;font-size:12px;letter-spacing:.8px;text-decoration:none;text-align:center}
.hero .btn{margin-top:22px;width:154px;height:40px;line-height:40px}

.why{position:absolute;top:584px;left:0;width:1200px;height:474px}
.section-ghost{position:absolute;top:50px;left:0;width:1200px;text-align:center;font-family:"Playfair Display",serif;font-size:48px;letter-spacing:14px;color:var(--faint)}
.section-title{position:absolute;top:80px;left:0;width:1200px;text-align:center;font-size:20px;font-weight:600;letter-spacing:4px;color:var(--ink)}
.section-rule{position:absolute;top:109px;left:527px;width:146px;height:1px;background:#d5d5d5}
.section-rule::after{content:"";position:absolute;left:44px;top:-.5px;width:58px;height:2px;background:#444}
.features{position:absolute;top:148px;left:150px;width:900px;display:flex}
.feature{width:225px;text-align:center}
.feature svg{width:44px;height:44px;stroke:var(--red);fill:none;stroke-width:1.6;stroke-linecap:round;stroke-linejoin:round}
.feature h3{margin-top:18px;font-size:12px;font-weight:600;color:var(--ink)}
.feature p{margin-top:22px;font-size:11px;line-height:18.5px;color:var(--text);padding:0 8px}
.why .btn{position:absolute;left:543px;top:358px;width:114px;height:36px;line-height:36px}

.area{position:absolute;top:1058px;left:0;width:1200px;height:142px}
.area-map{position:absolute;left:0;top:0;width:688px;height:142px;background:linear-gradient(135deg,#dcdcdc,#cfd6cf 60%,#d6d6d6)}
.area-panel{position:absolute;left:688px;top:0;width:512px;height:142px;background:var(--panel)}
.area-title{position:absolute;left:46px;top:76px;font-size:20px;line-height:24px;font-weight:700;color:var(--ink)}
.area-title span{color:var(--red)}
</style>
</head>
<body>
<div class="page">
  <header class="site-header">
    <div class="brand"><span class="brand-mark"></span><span class="brand-name">TBNW</span></div>
    <nav class="main-nav">
      <a href="#" class="is-active">HOME</a>
      <a href="#">SERVICES</a>
      <a href="#">ABOUT TBNW</a>
      <a href="#">CONTACT US</a>
      <a href="#">BLOG</a>
      <a href="#">MARKET NEWS</a>
    </nav>
  </header>

  <section class="hero">
    <div class="hero-photo" role="img" aria-label="Upward view of a glass office tower against a blue sky"></div>
    <div class="hero-copy">
      <h1 class="hero-title">PROFESSIONAL OFFICE<strong>AND WAREHOUSE LEASING</strong></h1>
      <p class="hero-lead">Fast-track your search with tenant reps that only serve you, and specialize in the DFW area.</p>
      <a href="#" class="btn">CONTACT US NOW</a>
    </div>
  </section>

  <section class="why">
    <div class="section-ghost" aria-hidden="true">REPRESENTATION</div>
    <h2 class="section-title">WHY TENANT REPRESENTATION</h2>
    <div class="section-rule"></div>
    <div class="features">
      <div class="feature">
        <svg viewBox="0 0 44 44"><path d="M3 18l9-9 6 4 6-3 6 2 11 8-6 8"/><path d="M12 21l10 10a2 2 0 003-3M16 26l7 7a2 2 0 003-3M20 30l4 4a2 2 0 003-3M25 28l2 2a2 2 0 003-3l-9-9-4 3a2.5 2.5 0 01-3-4l6-5"/><path d="M3 18l6 7"/></svg>
        <h3>RELATIONSHIPS</h3>
        <p>Save time by trusting TBNW year after year to find the right location for you. Once we've worked together,</p>
      </div>
      <div class="feature">
        <svg viewBox="0 0 44 44"><circle cx="29" cy="14" r="10"/><circle cx="32" cy="11" r="3"/><path d="M22 21L6 37v4h5l1-3 3-1 1-3 3-1 1-3 4-4"/></svg>
        <h3>ACCESS TO MORE</h3>
        <p>We have no agreements or personal incentives for specific properties, so we can always show you the off...</p>
      </div>
      <div class="feature">
        <svg viewBox="0 0 44 44"><circle cx="24" cy="10" r="6"/><path d="M24 6v8M22 8h3a1.5 1.5 0 010 3h-2a1.5 1.5 0 000 3h3"/><path d="M4 30l10-8h8l10 4-2 3h-9"/><path d="M4 36l6-3 10 3 16-10 4 3-20 13-12-3"/></svg>
        <h3>FREE TO YOU</h3>
        <p>You pay us nothing. We get our com- mission from the property being leased.</p>
      </div>
      <div class="feature">
        <svg viewBox="0 0 44 44"><path d="M8 4l6 6-2 4 22 22a3 3 0 01-4 4L8 18l-4 2-2-6 4-2z"/><path d="M38 4a7 7 0 00-8 9L6 37a2 2 0 003 3l24-24a7 7 0 009-8l-4 4-4-1-1-4z"/></svg>
        <h3>CUSTOMIZED SERVICE</h3>
        <p>Aside from saving you the time of repeating what your needs are to each new location, we also provide...</p>
      </div>
    </div>
    <a href="#" class="btn">KNOW MORE</a>
  </section>

  <section class="area">
    <div class="area-map" role="img" aria-label="Street map of the Dallas Fort Worth area"></div>
    <div class="area-panel">
      <h2 class="area-title">IF YOU NEED TO FIND OFFICE<br>OR WAREHOUSE SPACE IN<br>THE <span>DALLAS FORT WORTH</span></h2>
    </div>
  </section>
</div>
</body>
</html>
```